FUN and creative designs WANTED! Mobile Marketing Start-up Company

Website design needed.

- PO is a full service mobile marketing agency in existence to help connect companies with their audience on unwired devices (Smartphone and tablets).

- PO is a start-up business with no current website looking to make a solid, memorable first impression.
Updates

Please take into consideration the following two points from our brief:

-  sense of humour and fun. Showing that mobile marketing for your business can be easy, interesting, and not just for big companies.

- a little ‘left of centre’ (i.e. NOT corporate!)

Thanks!

Please don't use black as a back groud. 

Target Market(s)

Primarily Media Agencies and Direct clients of all business types

Industry/Entity Type

Marketing

Requirements
Must have
• •The website should be: simple, clean yet a little ‘left of centre’ (i.e. NOT corporate!)
•Colour-in-line with PO logo (Black, Grey and orange: RBG: 255, 59, 0)
•Font: Arial and Aller Bold as per logo
•The website needs to show the charter of the business- sense of humour and fun. Showing that mobile marketing for your business can be easy, interesting, and not just for big companies.

What pages are required:
-Home Page
-Why Mobile
-Why Peyla
-Services
-Contact

* For initial submission only a home page and one sub-page is require as the other pages will work from the same template

* Coding would be great but not a essential
Nice to have
• Please suggest some stock photos for the website
Should not have
• Please review all attached documents:
* Full brief
* Logo files
* Web copy

```html
<!DOCTYPE html>
<html lang="en">
<head>
<meta charset="utf-8">
<title>Peyla Unwired – Mobile Marketing</title>
<link rel="stylesheet" href="https://fonts.googleapis.com/css2?family=Arimo:wght@400;700&display=swap">
<style>
:root{
  --orange:#ff3b00;
  --footer-orange:#e4580d;
  --footer-head:#8a3a10;
  --nav-red:#d10f0f;
  --nav-red-dark:#8c0303;
  --red-text:#e0261c;
  --ink:#222;
  --font:"Arimo",Arial,sans-serif;
}
*{box-sizing:border-box;margin:0;padding:0}
html,body{width:981px;height:1200px;overflow:hidden}
body{
  position:relative;font-family:var(--font);color:var(--ink);
  background:linear-gradient(#3a3a3a 0 5px,#fdfdfd 5px,#eeeeee 100px,#ff9a3c 100px,#ff8a1c 300px,#ff7a0a 370px,#bdbdbd 370px,#8a8a8a 700px,#3a3a3a 950px,#050505 1200px);
}
.abs{position:absolute}
a{text-decoration:none;color:inherit}
/* header */
.brand{left:115px;top:44px;display:flex;align-items:center;gap:8px}
.brand-dot{width:26px;height:26px;border-radius:50%;background:var(--orange);flex-shrink:0}
.brand-name{font-size:24px;font-weight:700;color:#333;white-space:nowrap}
.contact-item{top:31px;display:flex;align-items:center;gap:5px;font-size:11px;color:#666;white-space:nowrap}
.contact-item svg{display:block}
.search{left:645px;top:70px;width:178px;height:22px;border:1px solid #d8d8d8;background:#f0f0f0;display:flex}
.search span{flex:1;font-size:8px;color:#999;padding:6px 8px}
.search .btn{width:21px;background:#cfcfcf;display:flex;align-items:center;justify-content:center}
/* nav */
.main-nav{left:108px;top:104px;width:724px;height:35px;background:linear-gradient(var(--nav-red),var(--nav-red-dark));font-size:10.5px;color:#2a0000}
.main-nav a,.foot-nav a{position:absolute;white-space:nowrap}
.main-nav a{top:11px}
.main-nav .home{left:5px;top:6px;width:68px;height:23px;background:linear-gradient(#444,#111);color:#fff;display:flex;align-items:center;justify-content:center;font-size:11px}
/* hero */
.hero{left:108px;top:139px;width:724px;height:301px;background:linear-gradient(#eef3f7,#dde6ee 45%,#b7c8d6 47%,#d4e2ec);box-shadow:0 4px 6px rgba(0,0,0,.25)}
.hero-devices{position:absolute;left:78px;top:6px;width:620px;height:210px;background:linear-gradient(100deg,#26292d,#4a5560 40%,#3a6f9a 75%,#1d2226);border-radius:6px;opacity:.85}
.hero-title{position:absolute;left:73px;top:217px;font-size:35px;font-weight:400;color:var(--red-text);white-space:nowrap}
.hero-sub{position:absolute;left:74px;top:260px;font-size:13px;color:#222;line-height:15px}
.hero-arrow{position:absolute;width:29px;height:29px;border-radius:50%;background:var(--orange);display:flex;align-items:center;justify-content:center}
/* content */
.content{left:108px;top:440px;width:724px;height:445px;background:linear-gradient(#ececec,#dcdcdc)}
.intro-title{position:absolute;left:18px;top:18px;font-size:18px;font-weight:400;color:#222}
.intro-art{position:absolute;left:30px;top:50px;width:112px;height:112px;border-radius:50%;background:radial-gradient(#cfd8e3,#9fb4cc 70%,#e2e2e2 71%)}
.intro-text{position:absolute;left:162px;top:49px;width:520px;font-size:10.5px;line-height:11.4px;color:#333}
.contact-btn{position:absolute;left:324px;top:125px;width:340px;height:27px;border:1px solid #999;border-radius:5px;background:linear-gradient(#fff,#e6e6e6);font-size:13px;color:#666;display:flex;align-items:center;justify-content:center}
.col-title{position:absolute;top:175px;font-size:20px;font-weight:400;color:#222}
.col-img{position:absolute;border:2px solid var(--orange);background:#fff;padding:3px}
.col-img div{width:100%;height:100%}
.col-text{position:absolute;font-size:8.6px;line-height:10.3px;color:#333}
.more{position:absolute;font-size:9px;color:var(--orange)}
/* footer */
.footer{left:108px;top:885px;width:724px;height:235px;background:var(--footer-orange)}
.foot-head{position:absolute;top:27px;font-size:11px;font-weight:700;color:var(--footer-head)}
.foot-rule{position:absolute;left:0;top:46px;width:720px;height:1px;background:#f3a07a}
.foot-div{position:absolute;top:47px;width:1px;height:122px;background:#f3a07a}
.foot-list{position:absolute;top:60px;list-style:none;font-size:8.3px;line-height:15px;color:#fff}
.foot-list.bullets li{padding-left:14px;position:relative}
.foot-list.bullets li::before{content:"»";position:absolute;left:0;color:#ffb07a}
.foot-contact{position:absolute;left:552px;top:55px;color:#fff;font-weight:700;font-size:9px;line-height:15px}
.foot-contact strong{font-size:13px;display:block;line-height:17px}
.foot-nav{position:absolute;left:0;top:214px;width:724px;height:14px;font-size:10.5px;color:#1a0800}
.foot-nav .home{color:#fff}
/* bottom bar */
.bottom-bar{left:108px;top:1120px;width:724px;height:80px;background:linear-gradient(#bcbcbc,#f2f2f2 40%,#e0e0e0)}
.bottom-brand{position:absolute;left:16px;top:30px;display:flex;align-items:center;gap:6px}
.bottom-brand .brand-dot{width:20px;height:20px}
.bottom-brand .brand-name{font-size:22px}
.copy{position:absolute;left:357px;top:37px;font-size:10.5px;color:#777;white-space:nowrap}
.social{position:absolute;left:570px;top:33px;display:flex;gap:5px}
.social span{width:19px;height:19px;border-radius:3px}
</style>
</head>
<body>

<header>
  <div class="abs brand"><span class="brand-dot"></span><span class="brand-name">PEYLA UNWIRED</span></div>
  <div class="abs contact-item" style="left:576px">
    <svg width="20" height="20" viewBox="0 0 20 20"><circle cx="10" cy="10" r="9" fill="none" stroke="#333" stroke-width="1.5"/><path d="M7 5c-1 1-1 3 1 6s4 4 5 3l1-1-2-2-1 1c-1 0-3-2-3-3l1-1-2-2z" fill="#333"/></svg>
    <span>: 0211555018</span>
  </div>
  <div class="abs contact-item" style="left:676px">
    <svg width="23" height="16" viewBox="0 0 23 16"><rect x="1" y="1" width="21" height="14" fill="none" stroke="#333" stroke-width="1.5"/><path d="M1 1l10.5 8L22 1M1 15l8-7M22 15l-8-7" fill="none" stroke="#333" stroke-width="1.2"/></svg>
    <span>: Sales@peylaunwired.com</span>
  </div>
  <div class="abs search"><span>Search our site</span><div class="btn"><svg width="10" height="10" viewBox="0 0 10 10"><circle cx="4" cy="4" r="3" fill="none" stroke="#555" stroke-width="1.3"/><path d="M6 6l3 3" stroke="#555" stroke-width="1.5"/></svg></div></div>
</header>

<nav class="abs main-nav">
  <a class="home" href="#">Home</a>
  <a href="#" style="left:85px">Mobile Strategy Mobile Training &amp; Research</a>
  <a href="#" style="left:293px">Full management</a>
  <a href="#" style="left:376px">Optimization</a>
  <a href="#" style="left:439px">Reporting and Insights</a>
  <a href="#" style="left:552px">Creative</a>
  <a href="#" style="left:598px">Mobile brand building</a>
</nav>

<section class="abs hero">
  <div class="hero-devices" role="img" aria-label="Photo of tablets and smartphones held in hands"></div>
  <h1 class="hero-title">Unleash your mobile potential now</h1>
  <p class="hero-sub">Unleash your mobile potential now, get Peyla Unwired on 0200555019 &nbsp;now<br>&nbsp;or email: info@peyla.com</p>
  <span class="hero-arrow" style="left:19px;top:235px"><svg width="12" height="12" viewBox="0 0 12 12"><path d="M8 1L3 6l5 5" fill="none" stroke="#fff" stroke-width="2.5"/></svg></span>
  <span class="hero-arrow" style="left:671px;top:246px"><svg width="12" height="12" viewBox="0 0 12 12"><path d="M4 1l5 5-5 5" fill="none" stroke="#fff" stroke-width="2.5"/></svg></span>
</section>

<main class="abs content">
  <h2 class="intro-title">We’re all going unwired. Isn’t it time you &nbsp;connected…</h2>
  <div class="intro-art" role="img" aria-label="Illustration of smartphones surrounded by connected people and devices"></div>
  <div class="intro-text">
    <p>Your customers are less wired, more savvy, and more in control than ever before. They’re untied to (broadcast) programming schedules, un-tethered to local content and unbridled in their choice of doing what they want when they want.</p>
    <p>They’re totally mobile. (link to why mobile?) Unwired from traditional media but completely connected to their tablets, phones and smart devices.</p>
    <p>And that’s where, with Peyla Unwired, you can plug into the biggest opportunity your brand has had for years.</p>
  </div>
  <div class="contact-btn">Please feel free to contact us if you have any questions.</div>

  <h2 class="col-title" style="left:27px">Are you a marketer?</h2>
  <div class="col-img" style="left:29px;top:204px;width:167px;height:139px"><div role="img" aria-label="Photo of a businesswoman on top of rising blocks" style="background:linear-gradient(#fff 40%,#eee 60%,#f7a21b 100%)"></div></div>
  <p class="col-text" style="left:18px;top:354px;width:296px">Right now, you’re at the threshold of taking advantage of your brand’s most powerful marketing channel for decades. Peyla Unwired are your one-stop mobile partners on your mobile evolution and discovery.<br><br>We’re big on results, and even bigger on making everything thing simple for you. Unwired. Uncomplicated.</p>
  <a class="more" style="left:284px;top:422px">know more...</a>

  <h2 class="col-title" style="left:402px">Are you an agency?</h2>
  <div class="col-img" style="left:401px;top:203px;width:211px;height:136px"><div role="img" aria-label="Illustration of figures labelled advertiser, publisher, agency and developer" style="background:linear-gradient(90deg,#fff,#d8d8d8 30%,#fff 50%,#f38b2a 65%,#fff 75%,#d8d8d8 90%,#fff)"></div></div>
  <p class="col-text" style="left:400px;top:348px;width:292px">Integrating mobile marketing into your offering with Peyla Unwired, not only reinforces your credibility with your clients, it also helps them achieve more revenue from previously untapped markets. Which in turn, produces more profits for you.<br><br>We’re big on making things happen and even bigger on working with agencies to offer advertisers fully integrated mobile campaigns. Unwired. Unlocked.</p>
  <a class="more" style="left:656px;top:426px">know more...</a>
</main>

<footer class="abs footer">
  <span class="foot-head" style="left:31px">Services</span>
  <span class="foot-head" style="left:249px">Support</span>
  <span class="foot-head" style="left:394px">Company</span>
  <span class="foot-head" style="left:555px">Contact</span>
  <div class="foot-rule"></div>
  <div class="foot-div" style="left:231px"></div>
  <div class="foot-div" style="left:376px"></div>
  <div class="foot-div" style="left:528px"></div>
  <ul class="foot-list bullets" style="left:24px;width:190px">
    <li>Mobile Strategy/consultancy</li>
    <li>Mobile training and research</li>
    <li>Full management, optimization, reporting and insights</li>
    <li>Creative development and production</li>
    <li>Mobile brand building/brand development</li>
  </ul>
  <ul class="foot-list" style="left:251px">
    <li>Support Contacts</li><li>Product Registration</li><li>User Manuals</li><li>Software Downloads</li><li>Product Warranties</li>
  </ul>
  <ul class="foot-list" style="left:398px;top:58px">
    <li>Contact Us</li><li>About Us</li><li>Security and Privacy</li><li>Shipping and Returns</li><li>Terms of Use</li>
  </ul>
  <div class="foot-contact"><strong>PEYLA &nbsp;Unwired</strong>Address: Australia.<br>Phone:0400555020<br>E-mail: Sales@peylaunwired.com</div>
  <nav class="foot-nav">
    <a class="home" href="#" style="left:15px">Home</a>
    <a href="#" style="left:57px">Mobile Strategy Mobile Training &amp; Research</a>
    <a href="#" style="left:264px">Full management</a>
    <a href="#" style="left:348px">Optimization</a>
    <a href="#" style="left:409px">Reporting and Insights</a>
    <a href="#" style="left:523px">Creative</a>
    <a href="#" style="left:569px">Mobile brand building</a>
  </nav>
</footer>

<div class="abs bottom-bar">
  <div class="bottom-brand"><span class="brand-dot"></span><span class="brand-name">PEYLA</span></div>
  <p class="copy">PEYLA UNWIRED © 2012 &nbsp;&nbsp;| &nbsp;&nbsp;Privacy Policy</p>
  <div class="social">
    <span style="background:#555"></span>
    <span style="background:#2a6fd6"></span>
    <span style="background:#1a6fb0"></span>
    <span style="background:#f07a1a"></span>
  </div>
</div>

</body>
</html>
```